Single Page Production Company Site

Clean. Simple. Minimalist site with one page.

No portfolio, just some text to communicate a general overview of what the company does.

We work for a very select group of clients, creating strong brand personalities online. The site is specifically minimal and not communicating too much about what we do.. we have a variety of capabilities to work with clients and prefer to be broad with just a simple landing page as the point of contact for our brand.
Updates

Christmas holidays are coming up, maybe people need some time away from work with family and friends... We can keep working on this and I will provide feedback as quickly as possible, but I understand if designers have other commitments during the coming days. Thanks for your hard work!

Industry/Entity Type

Design Agency

Coding

Coded - Design and coding required

Number of Pages Required

1 page

Font styles to use
Sans Serif

Requirements
Must have
• Clean, bold text headlines.
Nice to have
• Unsure about any images used in the design, would like to see options with or without.

```html
<!DOCTYPE html>
<html lang="en">
<head>
<meta charset="utf-8">
<title>CEDAR Development</title>
<link href="https://fonts.googleapis.com/css2?family=Overlock:wght@900&family=Nunito+Sans:wght@400;600;800&family=Ubuntu:wght@500&display=swap" rel="stylesheet">
<style>
:root{
  --ink:#000000;
  --paper:#ffffff;
  --body-grey:#6b6b6b;
  --lead-grey:#555555;
  --rule:#bdbdbd;
  --art-light:#e6e6e6;
  --art-dark:#9a9a9a;
}
*{margin:0;padding:0;box-sizing:border-box}
html,body{width:1200px;height:2854px;overflow:hidden;background:var(--paper)}
body{position:relative;font-family:"Nunito Sans",sans-serif;color:var(--ink)}
.abs{position:absolute}
.display{font-family:"Overlock",sans-serif;font-weight:900;letter-spacing:.5px}

.hero{left:0;top:0;width:1200px;height:604px;background:var(--ink);color:var(--paper)}
.brand{left:80px;top:22px;font-family:"Ubuntu",sans-serif;font-weight:500;font-size:23px;letter-spacing:.6px}
.menu-icon{left:1101px;top:29px}
.hero-title{left:0;top:162px;width:1200px;text-align:center;font-size:90px;line-height:1}
.pillar{top:322px;width:310px}
.pillar h3{font-family:"Nunito Sans",sans-serif;font-weight:400;font-size:24px;margin-bottom:14px}
.pillar p{font-size:14px;line-height:25px}

.team-title{left:0;top:640px;width:1200px;text-align:center;font-size:64px}
.team-lead{left:200px;top:740px;width:800px;text-align:center;font-size:18px;line-height:29px;color:var(--lead-grey)}

.feature h2{font-size:60px;line-height:74px;margin-bottom:14px}
.feature p{font-size:13.5px;line-height:25px;color:var(--body-grey)}
.feature p+p{margin-top:15px}

.art{left:77px;top:1781px;width:469px;height:520px;background:linear-gradient(180deg,var(--art-light) 0%,#d4d4d4 50%,var(--art-dark) 100%)}

.contact{left:0;top:2239px;width:1200px;height:541px;background:var(--ink);color:var(--paper)}
.contact-title{left:0;top:138px;width:1200px;text-align:center;font-size:64px}
.contact-email{left:0;top:218px;width:1200px;text-align:center;font-size:20px;letter-spacing:.3px}
.contact-email svg{vertical-align:-6px;margin-right:20px}
.field{height:36px;border-bottom:1px solid var(--rule);font-size:13.5px;padding:6px 13px}
.send{left:506px;top:2660px;width:188px;height:47px;background:var(--paper);color:var(--ink);text-align:center;line-height:47px;font-family:"Nunito Sans",sans-serif;font-weight:800;font-size:20px;letter-spacing:.3px;z-index:2}

.footer{left:0;top:2808px;width:1200px;text-align:center;font-size:13px;color:var(--body-grey)}
</style>
</head>
<body>

<header class="abs hero">
  <div class="abs brand">CEDAR Development</div>
  <svg class="abs menu-icon" width="22" height="16" viewBox="0 0 22 16" aria-label="Menu"><rect y="0" width="22" height="2" fill="#fff"/><rect y="7" width="22" height="2" fill="#fff"/><rect y="14" width="22" height="2" fill="#fff"/></svg>
  <h1 class="abs hero-title display">concept.create.complete</h1>
  <div class="abs pillar" style="left:79px">
    <h3>design happens here</h3>
    <p>We are leading the way in design innovation for modern websites. Clean, functional, intuitive websites for progressive businesses.</p>
  </div>
  <div class="abs pillar" style="left:441px">
    <h3>art happens here</h3>
    <p>Building brands through design, we believe that contrast is everything. For industry leaders who set the pace and exceed expectations, we help give the company voice and soul.</p>
  </div>
  <div class="abs pillar" style="left:802px">
    <h3>ideas happen here</h3>
    <p>Clients look to us for unique, exceptional solutions to their technology issues. We bring creativity to the table and solve your business’ problems with actionable solutions.</p>
  </div>
</header>

<h2 class="abs team-title display">the cedar team</h2>
<p class="abs team-lead">Cedar Development Company focuses on creating extraordinary online experiences for extraordinary clients. We’ll work with you to create the perfect online presence for your brand.</p>

<section class="abs feature" style="left:594px;top:828px;width:505px">
  <h2 class="display">Size is<br>Everything.</h2>
  <p>We don’t work in a massive corporate office and we don’t have a mailroom. Not that there’s anything wrong with that, it’s just that we like knowing each other’s names, and encourage our clients to know ours. Our small staff has an advantage – our group works more efficiently, more cost-effectively and most importantly, flexible to each client’s unique needs. We deliver a range of services found at any agency, with the personal service you should expect.</p>
</section>

<section class="abs feature" style="left:110px;top:1172px;width:475px">
  <h2 class="display">Our Goal.</h2>
  <p>Cedar Development brings your brand to life, online. We do it all when it comes to online commerce for retail stores, wholesalers and distributors. Taking your company online introduces a world of opportunity, as well as specific challenges associated with online trade. We’ll assist you in establishing a successful online presence and bringing your brand to a worldwide audience.</p>
</section>

<section class="abs feature" style="left:445px;top:1434px;width:535px">
  <h2 class="display">Who's Miles?</h2>
  <p>Miles Harlow, owner of Cedar Development is not your typical principal. He’s worked internationally with both Halden House and Marlow Press publications in photo production for titles including Metropole and Gilded Review. Originally from coastal Maine and an all-around New Englander, Miles can often be found sailing during the summer and skiing during winter. He believes that inspiration comes from experiencing the world, not from sitting in a cubicle. But no worries, his biggest fear is being offline, and is always within an arms reach of the Internet.</p>
</section>

<section class="abs contact">
  <h2 class="abs contact-title display">Contact us</h2>
  <div class="abs contact-email">
    <svg width="32" height="22" viewBox="0 0 32 22" aria-hidden="true"><rect x="1" y="1" width="30" height="20" fill="none" stroke="#fff" stroke-width="1.5"/><path d="M1 1 L16 13 L31 1 M1 21 L12 10 M31 21 L20 10" fill="none" stroke="#fff" stroke-width="1.5"/></svg>hello@cedardevelopment.com
  </div>
  <div class="abs field" style="left:143px;top:273px;width:292px">Name</div>
  <div class="abs field" style="left:455px;top:273px;width:293px">Email</div>
  <div class="abs field" style="left:768px;top:273px;width:292px">Phone</div>
  <div class="abs field" style="left:143px;top:356px;width:917px">Message</div>
</section>

<div class="abs art" role="img" aria-label="Illustration of crumpled paper light bulbs hanging from cords, one glowing yellow"></div>

<section class="abs feature" style="left:623px;top:1836px;width:505px">
  <h2 class="display">We get you</h2>
  <p>Having a website isn't enough. You need to show your customers you understand the socially connected online world we live in.</p>
  <p>We help you create designs that capture the personality of your business and project the image you want your customers to see. Maybe you're a small company looking to sell yourself in the big leagues; maybe you're a big company that wants to look approachable; either way, we can make it happen.</p>
  <p>You'll come across looking professional, unique and strikingly hip all at the same time.</p>
</section>

<div class="abs send">SEND NOW</div>

<footer class="abs footer">2018 ©CEDAR Development - All Rights Reserved.</footer>

</body>
</html>
```